K&T Fixit and Rebuild general contracting business card design

I already have a logo that I want to use and I need a card that uses that logo and color scheme on the front with the address phone numbers and email and on the back a place for technicians to write in their name and phone number when they hand it out. It will need the License number of License #KTFXTRB318QN.
It should say General Contractor under the company name. The address is
4417 NE 3rd Ave, Ste D246
Vancouver, WA 98612
www.kandtfixitandrebuild.example
office@kandtfixitandrebuild.example
360-555-0182 is the telephone number
360-555-0149 is the fax number

Target Market(s)

Homeowners needing remodel work or repairs in their home.

Industry/Entity Type

Construction

Contact Information for Business Card

Business name, address, phone number, license number, fax number, email, and website on the front and a place to fill in technician's name and number

Font styles to use
Serif

Requirements
Must have
• Business name, address, phone number, license number, fax number, email, and website on the front and a place to fill in technician's name and number
Nice to have
• I uploaded an example of a front that is good.
Should not have
• Froo froo or extra embellishments.

```html
<!DOCTYPE html>
<html lang="en">
<head>
<meta charset="utf-8">
<title>K&amp;T Fixit and Rebuild — Business Card</title>
<link rel="stylesheet" href="https://fonts.googleapis.com/css2?family=Arimo:wght@400;700&family=Michroma&display=swap">
<style>
  :root {
    --maroon: #6e1028;
    --maroon-deep: #560c1f;
    --white: #ffffff;
    --white-soft: rgba(255,255,255,0.85);
    --grey-bg: #2e2e2e;
  }
  * { box-sizing: border-box; margin: 0; padding: 0; }
  html, body { width: 1200px; height: 900px; overflow: hidden; }
  body {
    background: radial-gradient(ellipse at 50% 40%, #4a4a4a 0%, var(--grey-bg) 75%);
    font-family: "Arimo", Arial, sans-serif;
    position: relative;
  }
  .card {
    position: absolute;
    left: 250px;
    width: 700px;
    height: 400px;
    box-shadow: 0 14px 30px rgba(0,0,0,0.45);
    overflow: hidden;
  }
  .card-front { top: 40px; display: flex; }
  .card-back {
    top: 470px;
    background: linear-gradient(135deg, var(--maroon) 0%, var(--maroon-deep) 100%);
    color: var(--white);
    display: flex; flex-direction: column; align-items: center; justify-content: center;
    padding: 0 90px;
  }
  .brand-panel {
    width: 270px;
    background: var(--white);
    display: flex; flex-direction: column; align-items: center; justify-content: center;
    padding: 24px;
    position: relative;
  }
  .brand-name {
    font-weight: 700;
    color: var(--maroon);
    font-size: 30px;
    line-height: 1.15;
    text-align: center;
    letter-spacing: 0.5px;
  }
  .brand-tagline {
    margin-top: 10px;
    font-weight: 400;
    color: var(--maroon);
    font-size: 15px;
    letter-spacing: 2px;
    text-transform: uppercase;
    text-align: center;
  }
  .brand-panel::after {
    content: "";
    position: absolute;
    right: -12px; top: 84px;
    border-left: 12px solid var(--white);
    border-top: 10px solid transparent;
    border-bottom: 10px solid transparent;
    z-index: 2;
  }
  .details-panel {
    flex: 1;
    background: linear-gradient(135deg, var(--maroon) 0%, var(--maroon-deep) 100%);
    color: var(--white);
    padding: 78px 30px 28px 40px;
  }
  .person-name {
    font-family: "Michroma", "Arimo", sans-serif;
    font-weight: 400;
    font-size: 23px;
    letter-spacing: 1px;
    line-height: 1;
    white-space: nowrap;
  }
  .person-role { font-size: 16px; margin-top: 6px; }
  .address { font-size: 17px; line-height: 1.3; margin-top: 16px; }
  .contact-list { list-style: none; margin-top: 10px; font-size: 17px; line-height: 1.35; }
  .contact-list li { display: flex; align-items: center; gap: 8px; white-space: nowrap; }
  .contact-list svg { width: 13px; height: 13px; fill: var(--white); flex: none; }
  .license { margin-top: 12px; font-size: 15px; letter-spacing: 0.5px; color: var(--white-soft); }
  .back-name {
    font-weight: 700;
    font-size: 40px;
    letter-spacing: 1px;
    text-align: center;
  }
  .back-tagline {
    margin-top: 8px;
    font-size: 16px;
    letter-spacing: 3px;
    text-transform: uppercase;
    color: var(--white-soft);
  }
  .write-in { width: 100%; margin-top: 40px; }
  .write-in-row { display: flex; align-items: flex-end; gap: 14px; margin-top: 26px; }
  .write-in-label { font-size: 17px; width: 110px; flex: none; }
  .write-in-line { flex: 1; border-bottom: 1.5px solid var(--white-soft); height: 20px; }
</style>
</head>
<body>
  <section class="card card-front" aria-label="Business card front">
    <div class="brand-panel">
      <p class="brand-name">K&amp;T Fixit<br>and Rebuild</p>
      <p class="brand-tagline">General Contractor</p>
    </div>
    <div class="details-panel">
      <h1 class="person-name">DANA WHITLOCK</h1>
      <p class="person-role">Director</p>
      <p class="address">4417 NE 3rd Ave, Ste D246<br>Vancouver, WA 98612</p>
      <ul class="contact-list">
        <li><svg viewBox="0 0 24 24" aria-hidden="true"><path d="M6.6 10.8a15 15 0 0 0 6.6 6.6l2.2-2.2c.3-.3.7-.4 1-.2 1.1.4 2.3.6 3.6.6.6 0 1 .4 1 1V20c0 .6-.4 1-1 1A17 17 0 0 1 3 4c0-.6.4-1 1-1h3.5c.6 0 1 .4 1 1 0 1.3.2 2.5.6 3.6.1.3 0 .7-.2 1z"/></svg>360-555-0182</li>
        <li><svg viewBox="0 0 24 24" aria-hidden="true"><path d="M6 2h12v6H6zM4 9h16a2 2 0 0 1 2 2v7h-4v4H6v-4H2v-7a2 2 0 0 1 2-2zm4 8v3h8v-3z"/></svg>360-555-0149</li>
        <li><svg viewBox="0 0 24 24" aria-hidden="true"><path d="M2 5h20v14H2zm2 2v.5l8 5 8-5V7zm0 2.8V17h16V9.8l-8 5z"/></svg>office@kandtfixitandrebuild.example</li>
        <li><svg viewBox="0 0 24 24" aria-hidden="true"><path d="M12 2a10 10 0 1 0 0 20 10 10 0 0 0 0-20zm6.9 6h-3a15 15 0 0 0-1.3-3.9A8 8 0 0 1 18.9 8zM12 4c.8 1.1 1.5 2.5 1.9 4h-3.8c.4-1.5 1.1-2.9 1.9-4zM4.3 14a8 8 0 0 1 0-4h3.4a16 16 0 0 0 0 4zm.8 2h3a15 15 0 0 0 1.3 3.9A8 8 0 0 1 5.1 16zm3-8h-3a8 8 0 0 1 4.3-3.9A15 15 0 0 0 8.1 8zM12 20c-.8-1.1-1.5-2.5-1.9-4h3.8c-.4 1.5-1.1 2.9-1.9 4zm2.3-6H9.7a14 14 0 0 1 0-4h4.6a14 14 0 0 1 0 4zm.3 5.9a15 15 0 0 0 1.3-3.9h3a8 8 0 0 1-4.3 3.9zm1.7-5.9a16 16 0 0 0 0-4h3.4a8 8 0 0 1 0 4z"/></svg>www.kandtfixitandrebuild.example</li>
      </ul>
      <p class="license">License #KTFXTRB318QN</p>
    </div>
  </section>

  <section class="card card-back" aria-label="Business card back">
    <p class="back-name">K&amp;T Fixit and Rebuild</p>
    <p class="back-tagline">General Contractor</p>
    <div class="write-in">
      <div class="write-in-row"><span class="write-in-label">Technician</span><span class="write-in-line"></span></div>
      <div class="write-in-row"><span class="write-in-label">Phone</span><span class="write-in-line"></span></div>
    </div>
  </section>
</body>
</html>
```